Gaming Headset Packaging Design

We would like a gaming window box style packaging design for our gaming headset.

We want to use the packaging for 2-3 of our gaming headphone series and hence we would not like to put any product pictures on the packaging.

Size: (enclosed die-cut drawing) please feel free to modify the shape of the window
Material: E Flute Paper box
Type: Window Box style
Design features we prefer: gaming, playful, creative, trendy, High tech.
Requirement: AI file is preferred

Enclosed are a detailed description along with competitor designs and existing die-cut drawing (AI format) for your reference.

Any further questions, please feel free to ask.

```html
<!DOCTYPE html>
<html lang="en">
<head>
<meta charset="utf-8">
<title>Pro Gaming Headset 7.1 – Window Box Dieline</title>
<link rel="stylesheet" href="https://fonts.googleapis.com/css2?family=Audiowide&family=Barlow+Condensed:wght@400;500;700&display=swap">
<style>
  :root {
    --cyan: #13aee0;
    --ink: #0e1319;
    --window: #5f6061;
    --white: #ffffff;
    --stage: #2b2b2d;
    --display: "Audiowide", sans-serif;
    --body: "Barlow Condensed", sans-serif;
  }
  * { margin: 0; padding: 0; box-sizing: border-box; }
  html, body { width: 1200px; height: 1200px; overflow: hidden; background: var(--stage); }
  .canvas { position: relative; width: 1200px; height: 1200px; }
  .dieline {
    position: absolute; left: 0; top: 362px;
    width: 1500px; height: 595px;
    transform: scale(0.8); transform-origin: 0 0;
    overflow: hidden;
  }
  .panel { position: absolute; top: 0; height: 595px; }

  /* side panel */
  .side-panel { left: 0; width: 243px; background: var(--cyan); overflow: hidden; }
  .side-title {
    position: absolute; left: -160px; top: 222px; width: 540px; height: 140px;
    transform: rotate(-90deg);
    font-family: var(--display); font-weight: 400; color: var(--ink);
    white-space: nowrap;
  }
  .side-title .line1 { position: absolute; left: 8px; top: 2px; font-size: 52px; line-height: 60px; }
  .side-title .line2 { position: absolute; left: 8px; top: 58px; font-size: 56px; line-height: 80px; }
  .side-title .big { font-size: 96px; margin-left: 6px; }

  /* front panel */
  .front-panel { left: 243px; width: 498px; background: var(--ink); }
  .title-band { position: absolute; left: 0; top: 32px; width: 284px; height: 84px; background: var(--cyan); }
  .title-text {
    position: absolute; left: 25px; top: 40px; width: 270px; height: 72px;
    font-family: var(--display); font-weight: 400; color: var(--ink); line-height: 34px;
  }
  .title-text .l1 { font-size: 24px; display: block; }
  .title-text .l2 { font-size: 31px; display: block; }
  .title-text .num { position: absolute; left: 196px; top: 10px; font-size: 42px; line-height: 60px; }
  .pixel { position: absolute; background: var(--cyan); }
  .features { position: absolute; left: 24px; top: 172px; list-style: none; }
  .features li {
    display: flex; align-items: center; height: 73px;
    font-family: var(--body); font-weight: 400; font-size: 13px; color: var(--white);
  }
  .features svg { width: 48px; height: 52px; margin-right: 6px; }
  .virtual {
    position: absolute; left: 20px; top: 514px; width: 184px;
    font-family: var(--display); font-weight: 400;
  }
  .virtual .word {
    display: block; font-size: 33px; line-height: 38px;
    color: var(--ink); -webkit-text-stroke: 1.6px var(--cyan);
  }
  .virtual .sub { display: block; font-size: 14.5px; color: var(--white); margin-top: 6px; white-space: nowrap; }
  .virtual-num {
    position: absolute; left: 206px; top: 507px; width: 59px; height: 63px;
    background: var(--cyan); color: var(--ink);
    font-family: var(--display); font-size: 34px; line-height: 70px; text-align: center;
  }
  .rule { position: absolute; height: 2px; background: var(--cyan); }

  /* window */
  .window-cut { left: 741px; width: 269px; background: var(--window); }

  /* back panel */
  .back-panel {
    left: 1010px; width: 490px; background-color: var(--ink);
    background-image:
      linear-gradient(rgba(255,255,255,0.025) 1px, transparent 1px),
      linear-gradient(90deg, rgba(255,255,255,0.025) 1px, transparent 1px);
    background-size: 30px 30px;
  }
  .spec-box { position: absolute; border: 3px solid var(--cyan); }
  .spec-list { position: absolute; font-family: var(--body); font-size: 13.5px; line-height: 19.8px; }
  .spec-list .row { display: flex; justify-content: space-between; }
  .spec-list dt { color: var(--cyan); }
  .spec-list dd { color: var(--white); }
  .hex-badge { position: absolute; }
  .warning-box {
    position: absolute; left: 162px; top: 452px; width: 303px; height: 48px;
    border: 1px solid var(--cyan); display: flex;
  }
  .warning-icon { width: 43px; background: var(--cyan); display: flex; align-items: center; justify-content: center; }
  .warning-text { padding: 4px 6px; font-family: var(--body); font-size: 5.4px; line-height: 7px; color: var(--white); }
  .warning-text p + p { margin-top: 6px; }
  .brand {
    position: absolute; left: 162px; top: 508px;
    font-family: var(--body); font-weight: 700; font-size: 9px; color: var(--white);
  }
  .brand-note {
    position: absolute; left: 162px; top: 521px; width: 160px;
    font-family: var(--body); font-size: 5.4px; line-height: 7px; color: var(--white);
  }
  .code-box { position: absolute; left: 30px; top: 548px; width: 132px; height: 35px; border: 1px solid var(--white); }
  .base-line { position: absolute; left: 162px; top: 548px; width: 230px; height: 1px; background: var(--white); }
  .base-divider { position: absolute; left: 325px; top: 508px; width: 1px; height: 40px; background: var(--white); }
</style>
</head>
<body>
<main class="canvas">
  <div class="dieline">

    <section class="panel side-panel">
      <h2 class="side-title"><span class="line1">PRO GAMING</span><span class="line2">HEADSET<span class="big">7.1</span></span></h2>
    </section>

    <section class="panel front-panel">
      <div class="title-band"></div>
      <div class="pixel" style="left:284px;top:32px;width:30px;height:84px"></div>
      <div class="pixel" style="left:314px;top:40px;width:20px;height:60px"></div>
      <div class="pixel" style="left:334px;top:52px;width:16px;height:16px"></div>
      <div class="pixel" style="left:334px;top:78px;width:10px;height:10px"></div>
      <div class="pixel" style="left:356px;top:42px;width:12px;height:12px"></div>
      <div class="pixel" style="left:372px;top:32px;width:10px;height:10px"></div>
      <div class="pixel" style="left:398px;top:32px;width:10px;height:10px"></div>
      <h1 class="title-text"><span class="l1">PRO GAMING</span><span class="l2">HEADSET</span><span class="num">7.1</span></h1>

      <ul class="features">
        <li>
          <svg viewBox="0 0 48 52"><polygon points="24,3 44,14 44,38 24,49 4,38 4,14" fill="none" stroke="#13aee0" stroke-width="3"/><circle cx="26" cy="26" r="8" fill="#fff"/><path d="M20 19a9 9 0 0 0 0 14" fill="none" stroke="#13aee0" stroke-width="3"/></svg>
          Soft and soothing earpads
        </li>
        <li>
          <svg viewBox="0 0 48 52"><polygon points="24,3 44,14 44,38 24,49 4,38 4,14" fill="none" stroke="#13aee0" stroke-width="3"/><text x="24" y="32" text-anchor="middle" font-family="Audiowide, sans-serif" font-size="15" fill="none" stroke="#13aee0" stroke-width="1.3">3D</text></svg>
          3D Sound Vibration
        </li>
        <li>
          <svg viewBox="0 0 48 52"><polygon points="24,3 44,14 44,38 24,49 4,38 4,14" fill="none" stroke="#13aee0" stroke-width="3"/><rect x="11" y="18" width="26" height="16" rx="2" fill="none" stroke="#fff" stroke-width="1.5"/><circle cx="19" cy="26" r="5" fill="none" stroke="#13aee0" stroke-width="2"/><circle cx="29" cy="26" r="5" fill="none" stroke="#fff" stroke-width="2"/></svg>
          Dual Drivers on each ear for accuracy
        </li>
        <li>
          <svg viewBox="0 0 48 52"><polygon points="24,3 44,14 44,38 24,49 4,38 4,14" fill="none" stroke="#13aee0" stroke-width="3"/><path d="M14 30v-4a10 10 0 0 1 20 0v4" fill="none" stroke="#fff" stroke-width="2"/><rect x="12" y="28" width="5" height="9" rx="2" fill="none" stroke="#fff" stroke-width="1.6"/><rect x="31" y="28" width="5" height="9" rx="2" fill="none" stroke="#fff" stroke-width="1.6"/></svg>
          Bendable Stainless-Steel headband
        </li>
      </ul>

      <div class="virtual"><span class="word">VIRTUAL</span><span class="sub">SORROUND SOUND</span></div>
      <div class="virtual-num">7.1</div>
      <div class="rule" style="left:265px;top:557px;width:150px"></div>
      <div class="pixel" style="left:378px;top:535px;width:12px;height:12px"></div>
      <div class="pixel" style="left:400px;top:540px;width:20px;height:20px"></div>
      <div class="pixel" style="left:412px;top:528px;width:14px;height:10px"></div>
      <div class="pixel" style="left:420px;top:560px;width:12px;height:12px"></div>
      <div class="pixel" style="left:404px;top:578px;width:14px;height:17px"></div>
      <div class="pixel" style="left:432px;top:535px;width:66px;height:60px"></div>
    </section>

    <section class="panel window-cut" role="img" aria-label="Die-cut window showing the headset inside the box"></section>

    <section class="panel back-panel">
      <div class="spec-box" style="left:180px;top:65px;width:233px;height:177px"></div>
      <dl class="spec-list" style="left:198px;top:83px;width:156px">
        <div class="row"><dt>Speaker Diameter</dt><dd>Ø40mm</dd></div>
        <div class="row"><dt>Impedance</dt><dd>32Ω + 15</dd></div>
        <div class="row"><dt>Sensitivity S.P.L.</dt><dd>113dB + 3dB</dd></div>
        <div class="row"><dt>Rated Power</dt><dd>20mW</dd></div>
        <div class="row"><dt>Aggregate capability</dt><dd>30mW</dd></div>
        <div class="row"><dt>Frequency Response</dt><dd>20-20kHz</dd></div>
        <div class="row"><dt>Plug Type</dt><dd>3.5mm Stereo</dd></div>
      </dl>
      <svg class="hex-badge" style="left:363px;top:68px" width="104" height="114" viewBox="0 0 104 114">
        <polygon points="52,4 98,30 98,84 52,110 6,84 6,30" fill="#0e1319" stroke="#13aee0" stroke-width="6"/>
        <path d="M30 66v-12a22 22 0 0 1 44 0v12" fill="none" stroke="#13aee0" stroke-width="3"/>
        <rect x="26" y="58" width="11" height="22" rx="4" fill="none" stroke="#13aee0" stroke-width="3"/>
        <rect x="67" y="58" width="11" height="22" rx="4" fill="none" stroke="#13aee0" stroke-width="3"/>
      </svg>

      <div class="spec-box" style="left:230px;top:262px;width:207px;height:175px"></div>
      <dl class="spec-list" style="left:261px;top:278px;width:160px">
        <div class="row"><dt>Microphone Unit</dt><dd>Q6 x 5mm</dd></div>
        <div class="row"><dt>Sensitivity S.P.L.</dt><dd>34dB + 3dB</dd></div>
        <div class="row"><dt>Impedance</dt><dd>&lt;2.2k</dd></div>
        <div class="row"><dt>Frequency Response</dt><dd>30-16kHz</dd></div>
        <div class="row"><dt>Standard Operating Voltage</dt><dd>4.5V</dd></div>
        <div class="row"><dt>S/N Ratio Z</dt><dd>60dB</dd></div>
        <div class="row"><dt>Plug Type 3.5mm</dt><dd>Stereo</dd></div>
      </dl>
      <svg class="hex-badge" style="left:150px;top:263px" width="104" height="114" viewBox="0 0 104 114">
        <polygon points="52,4 98,30 98,84 52,110 6,84 6,30" fill="#0e1319" stroke="#13aee0" stroke-width="6"/>
        <rect x="43" y="28" width="18" height="34" rx="9" fill="none" stroke="#13aee0" stroke-width="3"/>
        <path d="M36 52a16 16 0 0 0 32 0M52 68v12M42 82h20" fill="none" stroke="#13aee0" stroke-width="3"/>
        <path d="M47 40h10M47 46h10M47 52h10" stroke="#13aee0" stroke-width="2"/>
      </svg>

      <div class="warning-box">
        <div class="warning-icon">
          <svg width="26" height="22" viewBox="0 0 26 22"><path d="M13 2 24 20H2Z" fill="none" stroke="#0e1319" stroke-width="2"/><path d="M13 8v6M13 16v2" stroke="#0e1319" stroke-width="2"/></svg>
        </div>
        <div class="warning-text">
          <p><b>Warning:</b> Keep volume at a safe level. Loud sound may damage your hearing. Never use the headset while driving.</p>
          <p><b>Caution:</b> Opening or modifying the product may affect its performance. Specifications and design may change without notice.</p>
        </div>
      </div>

      <div class="brand">VANTEX</div>
      <p class="brand-note">Vantex components sample notes for product details, packaging and care guidance for every user.</p>
      <div class="base-divider"></div>
      <svg class="hex-badge" style="left:343px;top:508px" width="34" height="36" viewBox="0 0 34 36"><polygon points="17,2 31,10 31,26 17,34 3,26 3,10" fill="none" stroke="#fff" stroke-width="2"/></svg>
      <svg class="hex-badge" style="left:403px;top:515px" width="62" height="50" viewBox="0 0 62 50" fill="none" stroke="#fff" stroke-width="1.5"><path d="M1 10V1h9M52 1h9v9M1 40v9h9M61 40v9h-9"/></svg>
      <div class="code-box"></div>
      <div class="base-line"></div>
      <svg class="hex-badge" style="left:166px;top:556px" width="222" height="24" viewBox="0 0 222 24" fill="none" stroke="#fff" stroke-width="1.6">
        <polygon points="10,3 18,7.5 18,16.5 10,21 2,16.5 2,7.5"/>
        <polygon points="32,3 40,7.5 40,16.5 32,21 24,16.5 24,7.5"/>
        <polygon points="54,3 62,7.5 62,16.5 54,21 46,16.5 46,7.5"/>
        <polygon points="76,3 84,7.5 84,16.5 76,21 68,16.5 68,7.5"/>
        <polygon points="98,3 106,7.5 106,16.5 98,21 90,16.5 90,7.5"/>
        <polygon points="120,3 128,7.5 128,16.5 120,21 112,16.5 112,7.5"/>
        <polygon points="142,3 150,7.5 150,16.5 142,21 134,16.5 134,7.5"/>
        <polygon points="164,3 172,7.5 172,16.5 164,21 156,16.5 156,7.5"/>
        <polygon points="186,3 194,7.5 194,16.5 186,21 178,16.5 178,7.5"/>
        <polygon points="208,3 216,7.5 216,16.5 208,21 200,16.5 200,7.5"/>
      </svg>
    </section>

  </div>
</main>
</body>
</html>
```